Resealable bag design and logo for sports nutrition powders needed.

GOAL is to create a resealable 220mm x 360mm universal bag for low cost 1kg sports nutrition products. This one bag will be used for a few different protein, diet and sports nutrition products (powder) and the specific product name (eg. Whey Protein 80, Meal Replacement Shake, etc.) will be applied on the bag face as a separate WHITE glossy round sticker with BLACK text as product name. So the bag must have a designated area for the sticker. To minimize cost, only 2 print colours should be used on top of the aluminum foil bag. FULL DESCRIPTION BRIEF FILE ATTACHED

Target Market(s)

EU

Industry/Entity Type

Nutrition

Requirements
Must have
• 2 print cylinders

```html
<!DOCTYPE html>
<html lang="en">
<head>
<meta charset="utf-8">
<title>Kestrel Fitness – Resealable Bag, Front and Back</title>
<link rel="stylesheet" href="https://fonts.googleapis.com/css2?family=Archivo+Black&family=Crimson+Text:wght@400;700&display=swap">
<style>
  :root {
    --page: #ffffff;
    --foil-light: #e4e4e4;
    --foil-mid: #bdbdbd;
    --foil-dark: #8e8e8e;
    --ink-red: #d8262b;
    --ink-black: #111111;
    --sticker: #f4f4f4;
    --label: #f6f6f6;
  }
  * { margin: 0; padding: 0; box-sizing: border-box; }
  html, body {
    width: 1200px; height: 837px; overflow: hidden;
    background: var(--page);
  }
  .canvas { position: relative; width: 1200px; height: 837px; }
  .bag {
    position: absolute; top: 85px; width: 478px; height: 685px;
    border-radius: 6px; overflow: hidden;
    background: linear-gradient(160deg, var(--foil-light), var(--foil-mid) 45%, var(--foil-light) 70%, var(--foil-dark));
  }
  .bag--front { left: 112px; }
  .bag--back { left: 655px; }
  .bag__art { position: absolute; inset: 0; width: 100%; height: 100%; }
  .product-sticker {
    position: absolute; left: 36px; top: 195px;
    width: 190px; height: 190px; border-radius: 50%;
    background: var(--sticker); border: 7px solid var(--ink-black);
    display: flex; flex-direction: column; align-items: center; justify-content: center;
    font-family: "Archivo Black", sans-serif; color: var(--ink-black);
    text-align: center; line-height: 1;
  }
  .product-sticker__line1 { font-size: 40px; }
  .product-sticker__line2 { font-size: 27px; margin-top: 6px; }
  .product-sticker__line3 { font-size: 46px; margin-top: 6px; }
  .brand-band {
    position: absolute; left: 0; right: 0; top: 600px; height: 52px;
    background: linear-gradient(180deg, var(--foil-light), var(--foil-mid));
    border-top: 3px solid var(--ink-black); border-bottom: 3px solid var(--ink-black);
    display: flex; align-items: center; justify-content: center; gap: 10px;
  }
  .brand-band__mark { width: 12px; height: 12px; background: var(--ink-red); }
  .brand-band__name {
    font-family: "Archivo Black", sans-serif; font-size: 34px;
    color: var(--ink-black); letter-spacing: 1px;
  }
  .info-label {
    position: absolute; left: 82px; top: 290px; width: 310px; height: 237px;
    background: var(--label); border: 4px solid var(--ink-black); border-radius: 10px;
    padding: 12px 16px;
    font-family: "Crimson Text", serif; font-size: 10.5px; line-height: 1.3;
    color: var(--ink-black); text-align: center;
  }
  .info-label p + p { margin-top: 11px; }
  .info-label__web { font-weight: 700; font-size: 12px; }
</style>
</head>
<body>
<main class="canvas">

  <section class="bag bag--front">
    <svg class="bag__art" viewBox="0 0 478 685" aria-hidden="false">
      <defs>
        <linearGradient id="tri-front-top" x1="0" y1="0" x2="1" y2="1">
          <stop offset="0" stop-color="#b8b8b8"/>
          <stop offset="0.45" stop-color="#c8262b"/>
          <stop offset="1" stop-color="#1a1a1a"/>
        </linearGradient>
        <linearGradient id="tri-front-bottom" x1="0" y1="0" x2="1" y2="1">
          <stop offset="0" stop-color="#2a2a2a"/>
          <stop offset="0.5" stop-color="#c8262b"/>
          <stop offset="1" stop-color="#9a9a9a"/>
        </linearGradient>
      </defs>
      <polygon role="img" aria-label="Geometric triangle pattern in red, black and grey"
        points="0,0 478,0 478,30 0,240" fill="url(#tri-front-top)"/>
      <polygon role="img" aria-label="Geometric triangle pattern in red, black and grey"
        points="0,445 478,330 478,600 0,600" fill="url(#tri-front-bottom)"/>
      <line x1="0" y1="240" x2="478" y2="30" stroke="#111" stroke-width="6"/>
      <line x1="0" y1="445" x2="478" y2="330" stroke="#111" stroke-width="6"/>
      <rect x="0" y="655" width="478" height="30" fill="#c8262b"/>
    </svg>
    <div class="product-sticker">
      <span class="product-sticker__line1">WHEY</span>
      <span class="product-sticker__line2">PROTEIN</span>
      <span class="product-sticker__line3">80</span>
    </div>
    <div class="brand-band">
      <span class="brand-band__mark"></span>
      <span class="brand-band__name">KESTREL FITNESS</span>
    </div>
  </section>

  <section class="bag bag--back">
    <svg class="bag__art" viewBox="0 0 478 685" aria-hidden="false">
      <defs>
        <linearGradient id="tri-back-top" x1="0" y1="0" x2="1" y2="1">
          <stop offset="0" stop-color="#c8262b"/>
          <stop offset="0.5" stop-color="#1a1a1a"/>
          <stop offset="1" stop-color="#b0b0b0"/>
        </linearGradient>
        <linearGradient id="tri-back-bottom" x1="0" y1="0" x2="1" y2="1">
          <stop offset="0" stop-color="#9a9a9a"/>
          <stop offset="0.5" stop-color="#c8262b"/>
          <stop offset="1" stop-color="#1a1a1a"/>
        </linearGradient>
      </defs>
      <polygon role="img" aria-label="Geometric triangle pattern in red, black and grey"
        points="0,0 478,0 478,110 0,365" fill="url(#tri-back-top)"/>
      <polygon role="img" aria-label="Geometric triangle pattern in red, black and grey"
        points="0,520 478,260 478,600 0,600" fill="url(#tri-back-bottom)"/>
      <line x1="0" y1="365" x2="478" y2="110" stroke="#111" stroke-width="6"/>
      <line x1="0" y1="520" x2="478" y2="260" stroke="#111" stroke-width="6"/>
      <rect x="0" y="655" width="478" height="30" fill="#c8262b"/>
    </svg>
    <div class="info-label">
      <p>This premium quality KESTREL Fitness product is proudly<br>produced in EU by Northvale Foods LLC.</p>
      <p>KESTREL Fitness is a registered trademark of<br>Northvale Foods LLC.</p>
      <p>Contact us: info@kestrelfitness.eu<br>See www.kestrelfitness.eu for full contact details<br>and product information.</p>
      <p>This product should not be used as a total diet replacement.<br>Not suitable for children under the age of 16.<br>Consult your doctor first if pregnant, breastfeeding or using<br>any medication.</p>
      <p class="info-label__web">www.kestrelfitness.eu</p>
    </div>
    <div class="brand-band">
      <span class="brand-band__mark"></span>
      <span class="brand-band__name">KESTREL FITNESS</span>
    </div>
  </section>

</main>
</body>
</html>
```